CV Template

We need a graphic design to our new CV templates for our consultants. We are a small young Danish upcoming IT-business company making software solutions for our customers etc. You can visit our new website here: dev.lunavaerket.com, then you can see our web design, colors etc. I have attached a file for your inspiration :-) In the presentation I would like to have a picture of the employee, some text who descripe the profile/consultant and then I imagine that there is a table where we can write the employee's skills etc.

I would like the design to be "fresh & catchy" :-)

Looking forward to hear from you.

Best regards,
Sanne

```html
<!DOCTYPE html>
<html lang="en">
<head>
<meta charset="utf-8">
<title>Lunaværket – Consultant CV</title>
<link href="https://fonts.googleapis.com/css2?family=Carlito:wght@400;700&family=Open+Sans:wght@400;500&display=swap" rel="stylesheet">
<style>
  :root{
    --page:#eef1f6;
    --sheet:#ffffff;
    --blue:#0070c0;
    --brand:#5b8cc6;
    --rule:#8db3e2;
    --ink:#404040;
    --row-light:#fdf1e6;
    --row-dark:#fecb98;
  }
  *{box-sizing:border-box;margin:0;padding:0}
  html,body{width:902px;height:1200px;overflow:hidden}
  body{position:relative;background:var(--page);font-family:"Carlito",Calibri,sans-serif;color:var(--ink)}
  .brand{position:absolute;top:76px;left:631px;font-family:"Carlito",sans-serif;font-size:26px;color:var(--brand);letter-spacing:.5px}
  .sheet{position:absolute;left:110px;top:140px;width:704px;height:938px;background:var(--sheet);border-radius:48px}
  .content{position:absolute;left:65px;top:48px;width:588px}
  .section-title{font-size:21px;font-weight:700;color:var(--blue);padding-bottom:2px;border-bottom:1px solid var(--rule)}
  .intro{font-size:13px;margin-top:5px}
  .projects{width:588px;border-collapse:collapse;margin-top:16px;table-layout:fixed}
  .projects th{font-size:20px;font-weight:700;color:var(--blue);text-align:left;padding:0 0 1px 2px;border-bottom:1px solid var(--rule)}
  .projects th.gap{border:none}
  .projects td{font-size:13px;line-height:16.7px;vertical-align:top;padding:5px 8px 0 8px}
  .projects tr.light td{background:var(--row-light)}
  .projects tr.dark td{background:var(--row-dark)}
  .projects tr.first td{padding-top:8px}
  .the-end{margin-top:32px;border-top:1px solid var(--rule);border-bottom:1px solid var(--rule);text-align:center;font-size:20px;font-weight:700;color:var(--blue);padding:3px 0 1px}
  .footer{position:absolute;top:1091px;left:110px;display:flex;font-family:"Open Sans",sans-serif;font-size:12px;color:#222}
  .footer span{margin-right:27px}
</style>
</head>
<body>
  <div class="brand">Lunaværket</div>

  <main class="sheet">
    <div class="content">
      <h2 class="section-title">Past Projects</h2>
      <p class="intro">Emil has gained extensive experience through various past projects as listed below:</p>

      <table class="projects">
        <colgroup><col style="width:146px"><col style="width:10px"><col style="width:108px"><col style="width:8px"><col></colgroup>
        <thead>
          <tr><th>Date</th><th class="gap"></th><th>Role</th><th class="gap"></th><th>Description of achievement</th></tr>
        </thead>
        <tbody>
          <tr class="light first" style="height:189px">
            <td>Feb 2003 – June 2004</td><td></td><td>Project manager</td><td></td>
            <td>Lorem ipsum dolor sit amet, consectetur adipiscing elit. Suspendisse sem odio, dictum vel diam vitae, feugiat mollis diam. Donec suscipit mi et iaculis hendrerit. Morbi molestie elementum eleifend. Suspendisse eleifend est enim, sit amet ultricies enim<br><br>Nulla congue tortor urna, ut varius odio ornare elementum. Cras blandit ante nec scelerisque porta. Nam consequat vestibulum tempus. Etiam ac aliquet urna, euismod et ullamcorper vitae, ullamcorper sed nisi. Vestibulum malesuada elit sapien.</td>
          </tr>
          <tr class="dark" style="height:83px">
            <td>Feb 2006 – June 2007</td><td></td><td>Sales manager</td><td></td>
            <td>Nunc quis diam nec mi imperdiet ultricies sit amet et lacus. Sed at sem at augue malesuada rhoncus. Pellentesque ullamcorper auctor libero at mollis. Cras bibendum diam enim, id euismod nisl ullamcorper et.</td>
          </tr>
          <tr class="light" style="height:84px">
            <td>Feb 2006 – June 2007</td><td></td><td>Sales manager</td><td></td>
            <td>Ut posuere vel purus ullamcorper sollicitudin. Sed non mi ante. Proin aliquam ligula ac nisi venenatis, eget interdum arcu placerat. Duis nec tincidunt erat. Integer dapibus iaculis convallis. Suspendisse tristique tempor diam, quis consectetur quam.</td>
          </tr>
          <tr class="dark" style="height:83px">
            <td>Feb 2006 – June 2009</td><td></td><td>Head programmer</td><td></td>
            <td>Sed non mi ante. Proin aliquam ligula ac nisi venenatis, eget interdum arcu placerat. Duis nec tincidunt erat. Integer dapibus iaculis convallis. Suspendisse tristique tempor diam, quis consectetur quam.</td>
          </tr>
          <tr class="light" style="height:67px">
            <td>June 2009 - Present</td><td></td><td>Programmer</td><td></td>
            <td>Nulla congue tortor urna, ut varius odio ornare elementum. Cras blandit ante nec scelerisque porta. Nam consequat vestibulum tempus. Etiam ac aliquet urna, euismod et ullamcorper vitae</td>
          </tr>
          <tr class="dark" style="height:49px">
            <td>June 2009 - Present</td><td></td><td>Program developer</td><td></td>
            <td>Cras bibendum diam enim, id euismod nisl ullamcorper et. Ut posuere vel purus ullamcorper sollicitudin.</td>
          </tr>
        </tbody>
      </table>

      <div class="the-end">The End</div>
    </div>
  </main>

  <footer class="footer">
    <span>Lunaværket ApS</span>
    <span>Lindevej 12</span>
    <span style="margin-right:38px">2200 København N</span>
    <span style="margin-right:36px">Tel: +45 20 40 60 80</span>
    <span>www.lunavaerket.dk</span>
  </footer>
</body>
</html>
```